Reworking our Ayurvedic Tea Boxes with Mordern and New look.

We are a Tea Wholesale company for retailers and health food stores. We have currently a Ayurvedic wellness tea line needs an updated packaging. We would like to see new modern, clean and beautiful new fresh look. Our current packaging can be seen at http://leafmerchantco.example/c/7720815/1/herbal-blends.html

We are going to launch various categories in the loose leaf tea line. This is just the first step. At present 9 different exsit in the wellnes line.
Updates

Target Market(s)

Health Food Stores, Specialty Food Stores, Grocery Stores.

Industry/Entity Type

It Company

Requirements
Must have
• - Name of the of the tea type should be clearly visible.
• - A modern fresh look. Not to heavy with design work.
Nice to have
• Box size is 8 cm (L) X 4.5 cm (W) X 15cm (H)

```html
<!DOCTYPE html>
<html lang="en">
<head>
<meta charset="utf-8">
<title>Ayurvedic Tea – Loose Leaf Box Fronts</title>
<link rel="stylesheet" href="https://fonts.googleapis.com/css2?family=Advent+Pro:wght@500&family=Allura&family=Arimo:wght@400&family=Alegreya+Sans+SC:wght@500&display=swap">
<style>
  :root {
    --stage-top: #f4f4f4;
    --stage-bottom: #a6a6a6;
    --white: #ffffff;
    --leaf-green: #7cb82f;
    --ginger-bg: #c94f0b;
    --ginger-accent: #f6c91c;
    --cold-bg: #c9161f;
    --cold-accent: #42d2dc;
    --evening-bg: #a8169b;
    --evening-accent: #bde22c;
  }
  * { box-sizing: border-box; margin: 0; padding: 0; }
  html, body { width: 1200px; height: 848px; overflow: hidden; }
  body {
    background: linear-gradient(180deg, var(--stage-top) 0%, var(--stage-bottom) 100%);
    position: relative;
    font-family: "Arimo", Arial, sans-serif;
  }
  .box-front {
    position: absolute;
    top: 123px;
    width: 323px;
    height: 607px;
    background: var(--box-bg);
    color: var(--white);
    overflow: hidden;
  }
  .box-front--ginger { left: 68px; --box-bg: var(--ginger-bg); --accent: var(--ginger-accent); --name-size: 48px; }
  .box-front--cold { left: 432px; --box-bg: var(--cold-bg); --accent: var(--cold-accent); --name-size: 60px; }
  .box-front--evening { left: 795px; --box-bg: var(--evening-bg); --accent: var(--evening-accent); --name-size: 60px; }

  .mandala {
    position: absolute;
    left: 30px;
    top: -2px;
    width: 263px;
    height: 172px;
  }
  .line-title {
    position: absolute;
    top: 175px;
    width: 100%;
    text-align: center;
    font-family: "Advent Pro", "Arial Narrow", sans-serif;
    font-weight: 500;
    font-size: 31px;
    letter-spacing: 0.5px;
  }
  .tea-name {
    position: absolute;
    top: 248px;
    left: 10px;
    right: 10px;
    height: 60px;
    display: flex;
    align-items: center;
    justify-content: center;
    font-family: "Allura", cursive;
    font-weight: 400;
    font-size: var(--name-size);
    line-height: 1;
    color: var(--accent);
    white-space: nowrap;
  }
  .tea-type {
    position: absolute;
    top: 326px;
    width: 100%;
    text-align: center;
    font-size: 21px;
    letter-spacing: 0.3px;
  }
  .caffeine-note {
    position: absolute;
    top: 357px;
    width: 100%;
    text-align: center;
    font-size: 12.5px;
  }
  .tea-window {
    position: absolute;
    left: 0;
    top: 380px;
    width: 323px;
    height: 190px;
  }
  .leaf-sprig {
    position: absolute;
    left: 6px;
    top: 478px;
    width: 76px;
    height: 70px;
  }
  .brand-name {
    position: absolute;
    left: 8px;
    top: 553px;
    font-family: "Alegreya Sans SC", Arial, sans-serif;
    font-weight: 500;
    font-size: 23px;
    letter-spacing: 1.5px;
  }
  .net-weight {
    position: absolute;
    left: 8px;
    top: 584px;
    font-size: 11.5px;
  }
</style>
</head>
<body>

  <svg width="0" height="0" style="position:absolute">
    <defs>
      <linearGradient id="tea-fill" x1="0" y1="0" x2="1" y2="1">
        <stop offset="0" stop-color="#d4b06a"/>
        <stop offset="0.5" stop-color="#a88043"/>
        <stop offset="1" stop-color="#6e4f22"/>
      </linearGradient>
      <linearGradient id="sprig-fill" x1="0" y1="0" x2="1" y2="1">
        <stop offset="0" stop-color="#e4f05a"/>
        <stop offset="1" stop-color="#3f8f24"/>
      </linearGradient>
    </defs>
  </svg>

  <section class="box-front box-front--ginger">
    <svg class="mandala" viewBox="0 0 263 172" role="img" aria-label="Ornamental mandala flower motif in yellow">
      <path d="M0 0 H263 Q250 120 131.5 172 Q13 120 0 0 Z" fill="var(--accent)" opacity="0.75"/>
    </svg>
    <h2 class="line-title">Ayurvedic Tea</h2>
    <h1 class="tea-name">Ginger &amp; Lemon</h1>
    <p class="tea-type">LOOSE LEAF TEA</p>
    <p class="caffeine-note">Caffeine Free / Sans Cafeine</p>
    <svg class="tea-window" viewBox="0 0 323 190">
      <path d="M110 28 Q230 -4 323 8" fill="none" stroke="var(--accent)" stroke-width="5"/>
      <path d="M100 180 Q120 40 323 18 V120 Q250 185 100 180 Z" fill="url(#tea-fill)" role="img" aria-label="Photograph of dried loose leaf tea blend"/>
    </svg>
    <svg class="leaf-sprig" viewBox="0 0 76 70" role="img" aria-label="Illustration of fresh green tea leaves">
      <ellipse cx="38" cy="38" rx="34" ry="26" fill="url(#sprig-fill)"/>
    </svg>
    <p class="brand-name">Leaf Ritual</p>
    <p class="net-weight">Nett Weight 3.5 oz/Poids Net 100 g</p>
  </section>

  <section class="box-front box-front--cold">
    <svg class="mandala" viewBox="0 0 263 172" role="img" aria-label="Ornamental mandala flower motif in turquoise">
      <path d="M0 0 H263 Q250 120 131.5 172 Q13 120 0 0 Z" fill="var(--accent)" opacity="0.75"/>
    </svg>
    <h2 class="line-title">Ayurvedic Tea</h2>
    <h1 class="tea-name">Cold Season</h1>
    <p class="tea-type">LOOSE LEAF TEA</p>
    <p class="caffeine-note">Caffeine Free / Sans Cafeine</p>
    <svg class="tea-window" viewBox="0 0 323 190">
      <path d="M110 28 Q230 -4 323 8" fill="none" stroke="var(--accent)" stroke-width="5"/>
      <path d="M100 180 Q120 40 323 18 V120 Q250 185 100 180 Z" fill="url(#tea-fill)" role="img" aria-label="Photograph of dried loose leaf tea blend"/>
    </svg>
    <svg class="leaf-sprig" viewBox="0 0 76 70" role="img" aria-label="Illustration of fresh green tea leaves">
      <ellipse cx="38" cy="38" rx="34" ry="26" fill="url(#sprig-fill)"/>
    </svg>
    <p class="brand-name">Leaf Ritual</p>
    <p class="net-weight">Nett Weight 3.5 oz/Poids Net 100 g</p>
  </section>

  <section class="box-front box-front--evening">
    <svg class="mandala" viewBox="0 0 263 172" role="img" aria-label="Ornamental mandala flower motif in lime green">
      <path d="M0 0 H263 Q250 120 131.5 172 Q13 120 0 0 Z" fill="var(--accent)" opacity="0.75"/>
    </svg>
    <h2 class="line-title">Ayurvedic Tea</h2>
    <h1 class="tea-name">Evening Time</h1>
    <p class="tea-type">LOOSE LEAF TEA</p>
    <p class="caffeine-note">Caffeine Free / Sans Cafeine</p>
    <svg class="tea-window" viewBox="0 0 323 190">
      <path d="M110 28 Q230 -4 323 8" fill="none" stroke="var(--accent)" stroke-width="5"/>
      <path d="M100 180 Q120 40 323 18 V120 Q250 185 100 180 Z" fill="url(#tea-fill)" role="img" aria-label="Photograph of dried loose leaf tea blend"/>
    </svg>
    <svg class="leaf-sprig" viewBox="0 0 76 70" role="img" aria-label="Illustration of fresh green tea leaves">
      <ellipse cx="38" cy="38" rx="34" ry="26" fill="url(#sprig-fill)"/>
    </svg>
    <p class="brand-name">Leaf Ritual</p>
    <p class="net-weight">Nett Weight 3.5 oz/Poids Net 100 g</p>
  </section>

</body>
</html>
```